Business Card Design

We need a business card design for a business based in Perth Western Australia. We supply bookkeeping,office systems and procedures. This company is run by professional, vibrant woman which needs to come across when looking at this card.
This includes:
Bookkeeping,BAS,Super,Payroll,Group Certificates,Year End Preparation, Budgets,Planning
Staff training
Office Clean Up, Archiving,New Files and Systems
We would like to see designs that use the colours red mahogony(see Seal attachment), black and ivory
We want a Seal(old fashion wax seal) (see attached) with the letters TL engraved into this ,with our mission statement, 'We leave our mark of excellence'
Updates

Hi to all

Please note that Tidewell Ledgers e mail address should read:  tidewellledgers.wa@quillbox.net
Thanks

Industry/Entity Type

Fashion

Contact Information for Business Card

Tidewell Ledgers
Bookkeeping,Office Systems & Procedures
Perth WA
Freya
MOB: 0438 512 647
e mail: tidewellledgers@quillbox.net

```html
<!DOCTYPE html>
<html lang="en">
<head>
<meta charset="utf-8">
<title>Tidewell Ledgers – Business Card</title>
<link href="https://fonts.googleapis.com/css2?family=La+Belle+Aurore&family=Arimo:wght@700&family=Marcellus+SC&display=swap" rel="stylesheet">
<style>
  :root {
    --mahogany: #6e1426;
    --mahogany-dark: #4e0c19;
    --seal-light: #d5283a;
    --seal-mid: #b3101f;
    --seal-deep: #7c0612;
    --ivory: #fbf9f1;
    --ink: #1b1b1b;
    --flap-line: #e7e5dc;
    --swoosh: #ecebe5;
    --page: #ffffff;
  }
  * { box-sizing: border-box; margin: 0; padding: 0; }
  html, body { width: 977px; height: 1200px; overflow: hidden; background: var(--page); }
  .canvas { position: relative; width: 977px; height: 1200px; }

  .card {
    position: absolute; left: 120px; width: 790px;
    background: var(--ivory); border-radius: 8px; overflow: hidden;
    box-shadow: 3px 4px 5px rgba(0,0,0,0.45);
  }
  .card--front { top: 75px; height: 397px; }
  .card--back  { top: 495px; height: 423px; }
  .card svg.decor { position: absolute; inset: 0; }

  .script { font-family: "La Belle Aurore", cursive; color: var(--mahogany); position: absolute; white-space: nowrap; }
  .company-lines { left: 72px; top: 36px; font-size: 27px; line-height: 46px; }
  .person { left: 73px; top: 240px; font-size: 31px; }
  .contact { position: absolute; left: 66px; font-family: "Arimo", Arial, sans-serif; font-weight: 700; font-size: 19px; color: var(--ink); display: flex; align-items: center; gap: 5px; }
  .contact--phone { top: 279px; }
  .contact--email { top: 304px; }
  .contact svg { fill: var(--ink); }
  .tagline--front { right: 32px; top: 328px; font-size: 23px; }

  .seal { position: absolute; border-radius: 50%;
    background: radial-gradient(circle at 40% 35%, var(--seal-light), var(--seal-mid) 55%, var(--seal-deep));
    box-shadow: 3px 5px 8px rgba(0,0,0,0.35); }
  .seal--front { left: 520px; top: 135px; width: 170px; height: 166px; }
  .seal--back  { left: 344px; top: 186px; width: 116px; height: 114px; }

  .services { position: absolute; left: 0; right: 0; top: 24px; text-align: center; font-family: "Marcellus SC", serif; color: var(--mahogany); }
  .services h2 { font-weight: 400; font-size: 21px; line-height: 26px; }
  .services p { font-size: 14.5px; line-height: 20px; }
  .tagline--back { left: 0; right: 0; text-align: center; top: 320px; font-size: 23px; padding-right: 20px; }
</style>
</head>
<body>
<div class="canvas">

  <section class="card card--front">
    <svg class="decor" width="790" height="397" viewBox="0 0 790 397">
      <path d="M0 162 C60 215 140 232 240 218 C360 200 460 120 580 100 C680 84 740 130 790 198 C740 140 690 104 590 108 C470 128 380 212 250 226 C140 238 60 216 0 168 Z" fill="var(--mahogany)"/>
    </svg>
    <div class="script company-lines">Tidewell Ledgers<br>Office Systems &amp; Procedures<br>Perth WA</div>
    <div class="seal seal--front" role="img" aria-label="Red wax seal engraved with TL"></div>
    <div class="script person">Freya</div>
    <div class="contact contact--phone">
      <svg width="12" height="19" viewBox="0 0 12 19"><path d="M2 0h8a2 2 0 0 1 2 2v15a2 2 0 0 1-2 2H2a2 2 0 0 1-2-2V2a2 2 0 0 1 2-2zm0 2v13h8V2z"/></svg>
      0438 512 647
    </div>
    <div class="contact contact--email">
      <svg width="16" height="11" viewBox="0 0 16 11"><path d="M0 0h16v11H0z M0 0l8 6 8-6" /><path d="M0 0l8 6 8-6" fill="none" stroke="var(--ivory)" stroke-width="1.4"/></svg>
      tidewellledgers.wa@quillbox.net
    </div>
    <div class="script tagline--front">We leave our mark of excellence</div>
  </section>

  <section class="card card--back">
    <svg class="decor" width="790" height="423" viewBox="0 0 790 423">
      <path d="M0 0 L402 243 L790 0" fill="none" stroke="var(--flap-line)" stroke-width="2"/>
      <path d="M0 330 C150 250 300 280 470 330 C600 368 700 330 790 275 C700 345 600 392 460 350 C300 300 160 270 0 345 Z" fill="var(--swoosh)"/>
      <path d="M0 380 C180 330 330 360 500 395 C640 420 720 410 790 390" fill="none" stroke="var(--swoosh)" stroke-width="3"/>
      <path d="M0 312 C80 230 220 190 360 225 C460 250 560 325 650 338 C720 346 760 320 790 275 C765 330 720 354 650 346 C550 336 450 262 355 234 C220 200 90 240 0 318 Z" fill="var(--mahogany)"/>
    </svg>
    <div class="services">
      <h2>Office Systems &amp; Procedures</h2>
      <p>Bookkeeping-BAS-Super-Payroll-Group Certificates-Year<br>End Preparation-Budgets-Planning-Staff Training-<br>Office Clean Up-Archiving-New Files &amp; Systems</p>
    </div>
    <div class="seal seal--back" role="img" aria-label="Red wax seal engraved with TL"></div>
    <div class="script tagline--back">We leave our mark of excellence</div>
  </section>

</div>
</body>
</html>
```